Business card design needed

Our modern electrical contracting company requires business card design utilising our logo and incorporating our tag line "Service when you need it". We specialise in assisting our customers 24/7 offering a breakdown service.

Industry/Entity Type

Electrical

Contact Information for Business Card

Marcus Penhale, Electrical contractor,Tel: (08) 8456 3071, Fax: (08) 8679 4315, Mob 0438 562 740, Email: marcus.penhale@brightwirepower.com.au, Web: www.brightwirepower.com.au

Requirements
Must have
• we require a 2 sided card.
Front- Logo, tag line and contact information.
Rear- service when you need it! Call now for our 24/7 breakdown service

```html
<!DOCTYPE html>
<html lang="en">
<head>
<meta charset="utf-8">
<title>Brightwire Power – Business Card</title>
<link rel="stylesheet" href="https://fonts.googleapis.com/css2?family=Open+Sans:wght@300;600;700&display=swap">
<style>
  :root {
    --ink: #0b0b0b;
    --panel: #0a0a0a;
    --white: #ffffff;
    --brand-blue: #1f5ce8;
    --glow-blue: #3d6bff;
    --steel-dark: #1b1c1d;
    --steel-mid: #8d8f91;
    --steel-light: #e9e9e9;
  }
  * { margin: 0; padding: 0; box-sizing: border-box; }
  html, body {
    width: 1065px; height: 1200px; overflow: hidden;
    background: var(--white);
    font-family: "Open Sans", Arial, sans-serif;
  }
  .sheet { position: relative; width: 1065px; height: 1200px; }
  .card-side {
    position: absolute; left: 0; width: 1065px; overflow: hidden;
    background:
      radial-gradient(ellipse 420px 150px at 50% 42%, rgba(255,255,255,0.95), rgba(255,255,255,0) 100%),
      linear-gradient(to bottom, var(--steel-dark) 0%, #3a3b3c 18%, var(--steel-mid) 45%, #6f7173 62%, #b9babb 80%, var(--steel-light) 92%, var(--white) 100%);
  }
  .card-front { top: 0; height: 596px; }
  .card-back { top: 600px; height: 596px; }
  .brand-dot {
    position: absolute; left: 50%; border-radius: 50%;
    background: var(--brand-blue);
    transform: translateX(-50%);
  }
  .card-front .brand-dot { top: 37px; width: 138px; height: 138px; }
  .card-back .brand-dot { top: 50px; width: 164px; height: 164px; }
  .brand-name {
    position: absolute; left: 0; right: 0; text-align: center;
    color: var(--brand-blue); font-weight: 700; letter-spacing: 1px;
  }
  .card-front .brand-name { top: 200px; font-size: 46px; }
  .card-back .brand-name { top: 240px; font-size: 54px; }
  .holder-name {
    position: absolute; top: 290px; left: 0; right: 0; text-align: center;
    font-size: 50px; font-weight: 700; color: var(--ink);
  }
  .holder-role {
    position: absolute; top: 352px; left: 0; right: 0; text-align: center;
    font-size: 38px; font-weight: 300; color: var(--ink);
  }
  .info-panel {
    position: absolute; left: 24px; width: 1016px;
    background: var(--panel); color: var(--white);
    text-align: center;
    box-shadow: 0 -4px 10px -4px var(--glow-blue), 0 4px 10px -4px var(--glow-blue);
  }
  .info-panel::before, .info-panel::after {
    content: ""; position: absolute; left: 15%; right: 15%; height: 3px;
    background: linear-gradient(to right, transparent, var(--glow-blue), transparent);
  }
  .info-panel::before { top: -3px; }
  .info-panel::after { bottom: -3px; }
  .card-front .info-panel { top: 425px; height: 134px; padding-top: 27px; }
  .contact-line { font-size: 26px; font-weight: 600; line-height: 40px; white-space: nowrap; }
  .card-back .info-panel { top: 343px; height: 201px; padding-top: 24px; }
  .tagline { font-size: 44px; font-weight: 600; line-height: 58px; }
  .call-line { font-size: 44px; font-weight: 600; line-height: 78px; margin-top: 6px; }
  .call-line .hours { font-size: 64px; }
</style>
</head>
<body>
<div class="sheet">
  <section class="card-side card-front">
    <div class="brand-dot"></div>
    <div class="brand-name">BRIGHTWIRE POWER</div>
    <h1 class="holder-name">Marcus Penhale</h1>
    <p class="holder-role">Electrical contractor</p>
    <div class="info-panel">
      <p class="contact-line">Tel: (08) 8456 3071, Fax: (08) 8679 4315, Mob 0438 562 740,</p>
      <p class="contact-line">marcus.penhale@brightwirepower.com.au, www.brightwirepower.com.au</p>
    </div>
  </section>
  <section class="card-side card-back">
    <div class="brand-dot"></div>
    <div class="brand-name">BRIGHTWIRE POWER</div>
    <div class="info-panel">
      <p class="tagline">Service when you need it!</p>
      <p class="call-line">Call now for our <span class="hours">24/7</span> breakdown service</p>
    </div>
  </section>
</div>
</body>
</html>
```